Redo a PPT pres. - Real Estate in Brazil - Socially equitable investments in Social Housing

We need to redo the presentation attached. It is an institutional presentation to attract local and foreign investors to invest in Brazilian Social Housing Projects structured by our company "RTV".
A middle class of 100 million, a housing deficit of 9M, a strong political will & positive income generation trends constitute grounds for a significant demand in social housing.
This make a perfect scheme for investors to invest in Brazilian Social Housing.
"RTV", is a consulting "boutique" focused in Brazilian real estate, specialized in structuring, analyzing and originating Brazilian social housing projects.
RTV is part of the group RTP. RTP is structured to create value through each step of the residential real estate business - structuring, financing, sales, marketing and technology.
We would like to see designs that use mainly the color blue. The final design should communicate financial safety and professionalism. In order to reach our needs, the designer will need to have basic understanding of finance and investment in order to highlight the most important information.
The idea is to receive back the PPT with each page redesigned and an homogeneous identity.
To all designers,
Target Market(s)
Institutional Investors and wealthy individuals
Industry/Entity Type
Residential
Look and feel
Each slider illustrates characteristics of the customer's brand and the style your logo design should communicate.

```html
<!DOCTYPE html>
<html lang="en">
<head>
<meta charset="utf-8">
<title>RTV – Investor Presentation</title>
<link href="https://fonts.googleapis.com/css2?family=Arimo:ital,wght@0,400;0,700;1,400&display=swap" rel="stylesheet">
<style>
:root{
  --blue:#1c5ea8;
  --blue-dark:#134a8a;
  --blue-light:#6f9fd3;
  --sky:#d7e6f5;
  --text:#3b3b3b;
  --grey:#8a8a8a;
  --line:#c9d3de;
  --bg:#ffffff;
}
*{box-sizing:border-box;margin:0;padding:0}
html,body{width:1200px;height:494px;overflow:hidden;background:var(--bg)}
body{font-family:"Arimo",Arial,sans-serif;color:var(--text);position:relative}
.slide{position:absolute;top:48px;width:525px;height:400px;background:#fff;
  border:1px solid #e2e2e2;box-shadow:2px 3px 6px rgba(0,0,0,.18);overflow:hidden}
.slide--developers{left:45px}
.slide--team{left:630px}
.slide__header{position:absolute;left:0;top:0;width:100%;height:74px;background:var(--blue)}
.slide__skyline{position:absolute;right:0;top:0;width:200px;height:74px;
  background:linear-gradient(90deg,rgba(255,255,255,0),rgba(255,255,255,.35))}
.slide__title{position:absolute;left:22px;top:12px;color:#fff;font-size:21px;line-height:24px;font-weight:400}
.slide__title--single{top:25px;font-size:24px}
.slide__footer{position:absolute;left:24px;bottom:10px;font-size:13px;color:var(--blue);font-weight:700}
.slide__number{position:absolute;right:18px;bottom:12px;font-size:8px;color:var(--grey)}

/* process bar */
.process{position:absolute;left:12px;top:88px;width:500px;height:16px}
.process__band{position:absolute;left:0;top:0;width:478px;height:16px;
  background:linear-gradient(180deg,#f4f7fb,#dde6f0);border-top:1px solid #c7d3e0;border-bottom:1px solid #c7d3e0}
.process__label{position:absolute;top:2px;font-size:9.5px;color:var(--blue)}
.process__arrows{position:absolute;top:3px;font-size:8px;color:var(--blue);letter-spacing:-1px}
.connector{position:absolute;top:106px;width:0;height:22px;border-left:1px dotted var(--blue-light)}
.connector::after{content:"";position:absolute;left:-3px;bottom:-2px;width:5px;height:5px;border-radius:50%;background:var(--blue-light)}

.column{position:absolute;top:130px;width:154px;height:236px;border:1px solid var(--line);padding:7px 8px}
.column__lead{font-size:8px;line-height:10px;font-weight:700;color:var(--blue);margin-bottom:8px}
.column__list{list-style:none}
.column__list li{position:relative;padding-left:9px;font-size:7.6px;line-height:9.6px;margin-bottom:5px}
.column__list li::before{content:"";position:absolute;left:1px;top:3px;width:3px;height:3px;border-radius:50%;background:var(--text)}
.column__close{font-size:8px;line-height:10px;font-weight:700;color:var(--blue);margin-top:6px}

/* team */
.member{position:absolute;top:88px;width:160px}
.member__photo{width:58px;height:68px;margin:0 auto;background:linear-gradient(160deg,#c9c9c9,#8d8d8d);border:1px solid #bdbdbd}
.member__name{text-align:center;font-size:9px;font-weight:700;color:var(--blue);margin-top:5px}
.member__role{text-align:center;font-size:7.5px;font-style:italic;color:var(--grey);margin-bottom:6px}
.member__list{list-style:none}
.member__list li{position:relative;padding-left:8px;font-size:6.6px;line-height:8.2px;margin-bottom:3px}
.member__list li::before{content:"";position:absolute;left:1px;top:3px;width:2.5px;height:2.5px;border-radius:50%;background:var(--text)}
</style>
</head>
<body>

<section class="slide slide--developers">
  <header class="slide__header">
    <div class="slide__skyline" role="img" aria-label="Light city skyline silhouette"></div>
    <h1 class="slide__title">…hand in hand with small to mid-size<br>developers</h1>
  </header>

  <div class="process">
    <div class="process__band"></div>
    <span class="process__label" style="left:10px">Current Environment</span>
    <span class="process__arrows" style="left:118px">►►►</span>
    <span class="process__label" style="left:183px">Environment is changing</span>
    <span class="process__arrows" style="left:296px">►►►</span>
    <span class="process__label" style="left:375px">Goal</span>
    <span class="process__arrows" style="left:484px">►►►</span>
  </div>
  <span class="connector" style="left:100px"></span>
  <span class="connector" style="left:262px"></span>
  <span class="connector" style="left:428px"></span>

  <div class="column" style="left:22px">
    <p class="column__lead">Small to mid-size developers want to increase their ability to attract investors</p>
    <ul class="column__list">
      <li>They represent the majority of developers focused on social housing</li>
      <li>They benefit from many years of experience constructing social housing and strong local relationship with municipalities</li>
      <li>However, they are still organized as family businesses and do not have the capacity to attract investors. They finance their projects with their own resources or those of friends and family, limiting their possibility of development</li>
    </ul>
  </div>

  <div class="column" style="left:185px">
    <p class="column__lead">To succeed, they need to improve their management, accounting, and corporate governance</p>
    <ul class="column__list">
      <li>These companies are becoming more willing to reorganize</li>
      <li>They want professional management and accounting systems</li>
      <li>They are seeking other sources of financing</li>
      <li>They want to double the number of projects they are currently completing every year</li>
    </ul>
  </div>

  <div class="column" style="left:348px">
    <p class="column__lead">RTV offers both investment sourcing and business consulting focused on these developers</p>
    <ul class="column__list">
      <li>Small to mid-size developers are not under the radar of large local or international investment banks such as Meridia, Atlas Capital, Norton Trust etc.</li>
      <li>RTV has already identified 10 developers (construction) whose operational processes and professionalization meet the need of sophisticated investors</li>
    </ul>
    <p class="column__close">Working with RTV allows them to leverage their capacity and develop more projects annually</p>
  </div>

  <div class="slide__footer">RTV</div>
  <div class="slide__number">7</div>
</section>

<section class="slide slide--team">
  <header class="slide__header">
    <div class="slide__skyline" role="img" aria-label="Light city skyline silhouette"></div>
    <h1 class="slide__title slide__title--single">Team</h1>
  </header>

  <article class="member" style="left:18px">
    <div class="member__photo" role="img" aria-label="Portrait photo of Marcel Lorca"></div>
    <p class="member__name">Marcel Lorca</p>
    <p class="member__role">Fund Raising</p>
    <ul class="member__list">
      <li>Head of Harbor Equity Capital Markets in Brazil</li>
      <li>Since 2007, responsible for building the ECM platform in Brazil, for origination, marketing, strategy and deal execution</li>
      <li>Deal captain of over US$9B of equity raised via IPO and/or follow-ons for listed Brazilian companies</li>
      <li>Worked with global Harbor members to provide optimal financing solutions for Brazilian clients: structured pre-IPO investments and private equity opportunities with Middle East and Asian investors</li>
      <li>Degree in Applied Mathematics and Social Science from the University of Valmontier and a M.A. in Finance and International Economics from Northfield Institute</li>
    </ul>
  </article>

  <article class="member" style="left:184px">
    <div class="member__photo" role="img" aria-label="Portrait photo of Christian Van Horst"></div>
    <p class="member__name">Christian Van Horst</p>
    <p class="member__role">Structurer</p>
    <ul class="member__list">
      <li>CFO Solara Hotels Group in South America</li>
      <li>Led the biggest Brazilian retrofit project ever (Torre V9) and high-end French retrofit projects in Paris (Palais Verlaine, Hôtel de Sarlat)</li>
      <li>Managed the investments in construction and retrofit of more than 30 new hotels per year in Brazil</li>
      <li>Founded Bravia Invest, a consulting firm in Real Estate, helping non Brazilian investors structure their portfolios in Brazil</li>
      <li>Founded Horizon Brazil, with the aim of becoming the first player in the promising Brazilian retrofit market</li>
      <li>Graduated from Ecole Marceau Paris &amp; Lerins (with an MBA), France</li>
    </ul>
  </article>

  <article class="member" style="left:350px">
    <div class="member__photo" role="img" aria-label="Portrait photo of Dario Cunhal"></div>
    <p class="member__name">Dario Cunhal</p>
    <p class="member__role">Sales</p>
    <ul class="member__list">
      <li>13 years of experience as Commercial Manager and Director</li>
      <li>Commercial Director at Vertis Brazil Realty</li>
      <li>Responsible for 30% of the financial results of Vertis Brazil</li>
      <li>In charge of the "in house sales" of Vertis, 280 brokers</li>
      <li>Graduated in Civil Engineering Civil and MBA in Real Estate</li>
    </ul>
  </article>

  <div class="slide__footer">RTV</div>
  <div class="slide__number">8</div>
</section>

</body>
</html>
```